Brovique Rack Card

I would like to have my price list on part of the flyer if you can look on our website
WWW.BROVIQUEPA.COM
Eye Lash Extension Studio and Spa.

Facials
Waxing
Make Up
Bridal Packages
KEMO Lash Lift

```html
<!DOCTYPE html>
<html lang="en">
<head>
<meta charset="utf-8">
<title>Brovique Rack Card</title>
<link href="https://fonts.googleapis.com/css2?family=Playfair+Display:ital,wght@0,400;0,700;1,400&family=Dancing+Script:wght@500&display=swap" rel="stylesheet">
<style>
:root{
  --page:#e9e7e6;
  --card:#ffffff;
  --frame:#f2a9ca;
  --pink:#ee8dbf;
  --salmon:#f4a88c;
  --ink:#1e1e1e;
  --rule:#b9b9b9;
  --skin-light:#e2c3b3;
  --skin-dark:#c89c88;
  --gold:#b89a5a;
}
*{box-sizing:border-box;margin:0;padding:0}
html,body{width:1200px;height:1200px;overflow:hidden;background:var(--page)}
body{position:relative;font-family:'Playfair Display',Georgia,serif;color:var(--ink)}
.card{position:absolute;top:66px;width:513px;height:1068px;background:var(--card);box-shadow:0 2px 8px rgba(0,0,0,.12)}
.card--front{left:58px}
.card--back{left:629px}
.frame{position:absolute;left:22px;top:24px;width:469px;height:1021px;border:4px solid var(--frame)}
.abs{position:absolute}
.brand{position:absolute;left:0;width:513px;text-align:center}
.brand__mark{position:absolute;left:196px;width:122px;height:122px;border-radius:50%;background:#f6ecef}
.brand__name{font-size:29px;font-weight:700;letter-spacing:.3px;line-height:36px}
.brand__tag{font-size:11.5px;letter-spacing:.3px;margin-top:1px}
.divider{position:absolute;height:12px}
.divider svg{display:block;width:100%;height:12px}
.title{position:absolute;left:0;width:513px;text-align:center;font-weight:700;color:var(--salmon);letter-spacing:3px}
.head{font-size:11.5px;font-weight:700;color:var(--pink);text-transform:uppercase;letter-spacing:.3px;line-height:15.8px}
.list{font-style:italic;font-size:12px;line-height:15.8px}
.row{display:grid}
.col-lash .row{grid-template-columns:93px auto}
.col-tint .row{grid-template-columns:146px auto}
.col-wax{width:220px}
.col-wax .row{grid-template-columns:151px auto}
.vline{position:absolute;left:257px;top:324px;width:1.5px;height:408px;background:var(--rule)}
.facials{left:43px;width:430px}
.facials .row{grid-template-columns:330px 25px auto}
.facials .min{text-align:right;padding-right:13px;width:55px;margin-left:-30px}
.caps{font-weight:700;letter-spacing:.5px}
.gap{height:15.8px}
.peel-note{text-align:right;padding-right:46px}
.enh .row{grid-template-columns:152px auto}
.bridal .row{grid-template-columns:197px auto}
.photo{position:absolute;background:linear-gradient(160deg,#f1ece7,#e3d3c6 55%,#3a3433)}
.eye{position:absolute;top:704px;width:174px;height:158px;background:linear-gradient(180deg,var(--skin-light),var(--skin-dark))}
.script{position:absolute;left:300px;width:170px;text-align:center;font-family:'Dancing Script',cursive;color:var(--pink);font-size:15px;line-height:19px}
.contact{font-size:14.5px;line-height:25.5px}
.contact .row{grid-template-columns:76px auto}
.contact b{font-weight:700}
.partner{position:absolute;left:322px;top:945px;width:130px;text-align:center;font-size:14px;letter-spacing:1px;color:var(--gold);white-space:nowrap}
.partner-box{position:absolute;left:334px;top:983px;width:105px;height:39px;background:#111}
</style>
</head>
<body>

<section class="card card--front">
  <div class="frame"></div>
  <div class="brand__mark" style="top:56px"></div>
  <div class="brand" style="top:186px">
    <div class="brand__name">Brovique PA</div>
    <div class="brand__tag">Summit Lash Studio &amp; Spa</div>
  </div>

  <div class="divider" style="left:45px;width:423px;top:249px"><svg viewBox="0 0 423 12" preserveAspectRatio="none"><line x1="6" y1="6" x2="417" y2="6" stroke="#b9b9b9" stroke-width="1.5"/><path d="M0 6l8-4v8zM423 6l-8-4v8z" fill="#b9b9b9"/><circle cx="211" cy="6" r="3" fill="#b9b9b9"/></svg></div>
  <div class="title" style="top:262px;font-size:34px">MENU OF SERVICES</div>
  <div class="divider" style="left:45px;width:423px;top:306px"><svg viewBox="0 0 423 12" preserveAspectRatio="none"><line x1="6" y1="6" x2="417" y2="6" stroke="#b9b9b9" stroke-width="1.5"/><path d="M0 6l8-4v8zM423 6l-8-4v8z" fill="#b9b9b9"/><circle cx="211" cy="6" r="3" fill="#b9b9b9"/></svg></div>

  <div class="abs col-lash" style="left:56px;top:331px">
    <div class="head">Classic Lashes</div>
    <div class="list">
      <div class="row"><span>Classic Full Set</span><span>starting at $195.00</span></div>
      <div class="row"><span>2 Week Fill</span><span>starting at $90.00</span></div>
      <div class="row"><span>3 Week Fill</span><span>starting at $105.00</span></div>
    </div>
  </div>
  <div class="abs col-lash" style="left:56px;top:410px">
    <div class="head">Hybrid Lashes</div>
    <div class="list">
      <div class="row"><span>Hybrid Full Set</span><span>starting at $245.00</span></div>
      <div class="row"><span>2 Week Fill</span><span>starting at $95.00</span></div>
      <div class="row"><span>3 Week Fill</span><span>starting at $115.00</span></div>
    </div>
  </div>
  <div class="abs col-lash" style="left:56px;top:489px">
    <div class="head">Volume Lashes</div>
    <div class="list">
      <div>Russian Volume</div>
      <div class="row"><span>Full Set</span><span>starting at $300.00</span></div>
      <div class="row"><span>2 Week Fill</span><span>starting at $125.00</span></div>
      <div class="row"><span>3 Week Fill</span><span>starting at $135.00</span></div>
    </div>
  </div>
  <div class="abs col-lash" style="left:56px;top:583px;width:190px">
    <div class="row" style="grid-template-columns:149px auto"><span class="head" style="text-transform:none">KEMO Lash Lift</span><span class="list">$200.00</span></div>
  </div>
  <div class="abs col-tint" style="left:56px;top:615px">
    <div class="head">Tinting</div>
    <div class="list">
      <div class="row"><span>Eye Lash Tinting</span><span>$35.00</span></div>
      <div class="row"><span>Eye Brow Tinting</span><span>$30.00</span></div>
      <div class="row"><span>Henna Spa Brow Tint</span><span>$65.00</span></div>
    </div>
  </div>

  <div class="vline"></div>

  <div class="abs col-wax" style="left:281px;top:331px">
    <div class="head">Facial Waxing</div>
    <div class="list">
      <div class="row"><span>Eye Brow Wax</span><span>$25.00</span></div>
      <div class="row"><span>Eye Brow Tweezing</span><span>$25.00</span></div>
      <div class="row"><span>Lip Wax</span><span>$13.00</span></div>
      <div class="row"><span>Chin Wax</span><span>$13.00</span></div>
      <div class="row"><span>Nose Wax</span><span>$15.00</span></div>
      <div class="row"><span>Nose Wax (Gentlemen)</span><span>$20.00</span></div>
      <div class="row"><span>Cheeks</span><span>$24.00</span></div>
      <div class="row"><span>Side Burns</span><span>$15.00</span></div>
      <div class="row"><span>Ears</span><span>$12.00</span></div>
    </div>
  </div>
  <div class="abs col-wax" style="left:281px;top:505px">
    <div class="head">Body Waxing</div>
    <div class="list">
      <div class="row"><span>Underarm</span><span>$26.00</span></div>
      <div class="row"><span>Half Arm</span><span>$31.00</span></div>
      <div class="row"><span>Full Arm</span><span>$41.00</span></div>
      <div class="row"><span>Chest</span><span>$41.00+</span></div>
      <div class="row"><span>Back</span><span>$52.00+</span></div>
      <div class="row"><span>Bikini Bottom</span><span>$41.00+</span></div>
      <div class="row"><span>Thong</span><span>$52.00+</span></div>
      <div class="row"><span>Brazilian</span><span>$67.00+</span></div>
      <div class="row"><span>Bikini &amp; Full Leg</span><span>$113.00+</span></div>
      <div class="row"><span>Stomach Line</span><span>$11.00</span></div>
      <div class="row"><span>Half Leg</span><span>$57.00</span></div>
      <div class="row"><span>Full Leg</span><span>$83.00</span></div>
      <div class="row"><span>Feet &amp; Toes</span><span>$10.00</span></div>
    </div>
  </div>

  <div class="divider" style="left:45px;width:423px;top:738px"><svg viewBox="0 0 423 12" preserveAspectRatio="none"><line x1="6" y1="6" x2="417" y2="6" stroke="#b9b9b9" stroke-width="1.5"/><path d="M0 6l8-4v8zM423 6l-8-4v8z" fill="#b9b9b9"/><circle cx="211" cy="6" r="3" fill="#b9b9b9"/></svg></div>
  <div class="head" style="position:absolute;left:0;width:513px;text-align:center;top:759px">Signature Facials</div>

  <div class="abs facials list" style="top:790px">
    <div class="row"><span>Ultra Sensitive System Facial</span><span class="min">45 min</span><span>$95.00</span></div>
    <div class="row"><span>Oxygenating- Lightening Facial*</span><span class="min">55 min</span><span>$110.00</span></div>
    <div class="row"><span>Pumpkin Detox Facial</span><span class="min">55 min</span><span>$110.00</span></div>
    <div class="row"><span>AHA Peeling Treatment</span><span class="min">50 min</span><span>$110.00</span></div>
    <div class="row"><span>Grape Stem Cell Solutions Facial</span><span class="min">60 min</span><span>$115.00</span></div>
    <div class="row"><span>Hyaluronic Time Erase Complex Facial</span><span class="min">60 min</span><span>$115.00</span></div>
    <div class="gap"></div>
    <div class="row"><span><span class="caps">CRYSTAL</span> Microdermabrasion</span><span class="min">30 min</span><span>$110.00</span></div>
    <div class="row"><span><span class="caps">DIAMOND</span>&nbsp; Microdermabrasion</span><span class="min">30 min</span><span>$120.00</span></div>
    <div class="gap"></div>
    <div class="row"><span>Micro Crystal Deluxe</span><span class="min">60 min</span><span>$155.00</span></div>
    <div class="row"><span>Micro Diamond Deluxe</span><span class="min">60 min</span><span>$165.00</span></div>
    <div class="gap"></div>
    <div class="row"><span>Customized Peels</span><span class="min">30 min</span><span>$55.00</span></div>
    <div class="peel-note">Lactic | Mandelic | Glycolic Peels</div>
  </div>
</section>

<section class="card card--back">
  <div class="frame"></div>
  <div class="brand__mark" style="top:50px"></div>
  <div class="brand" style="top:180px">
    <div class="brand__name">Brovique PA</div>
    <div class="brand__tag">Summit Lash Studio &amp; Spa</div>
  </div>
  <div class="divider" style="left:126px;width:263px;top:241px"><svg viewBox="0 0 263 12" preserveAspectRatio="none"><line x1="6" y1="6" x2="257" y2="6" stroke="#b9b9b9" stroke-width="1.5"/><path d="M0 6l8-4v8zM263 6l-8-4v8z" fill="#b9b9b9"/><circle cx="131" cy="6" r="3" fill="#b9b9b9"/></svg></div>

  <div class="head" style="position:absolute;left:0;width:513px;text-align:center;top:264px">Facial Enhancements</div>
  <div class="abs enh list" style="left:163px;top:286px">
    <div class="row"><span>Facial Booster</span><span>$7.00</span></div>
    <div class="row"><span>24 kt. Gold Eye Zone</span><span>$25.00</span></div>
    <div class="row"><span>Eye and Lip Treatment</span><span>$20.00</span></div>
    <div class="row"><span>Micro-Current</span><span>$25.00</span></div>
  </div>

  <div class="divider" style="left:43px;width:427px;top:358px"><svg viewBox="0 0 427 12" preserveAspectRatio="none"><line x1="6" y1="6" x2="421" y2="6" stroke="#b9b9b9" stroke-width="1.5"/><path d="M0 6l8-4v8zM427 6l-8-4v8z" fill="#b9b9b9"/><circle cx="213" cy="6" r="3" fill="#b9b9b9"/></svg></div>
  <div class="title" style="top:368px;font-size:34px">BRIDAL</div>
  <div class="divider" style="left:43px;width:427px;top:408px"><svg viewBox="0 0 427 12" preserveAspectRatio="none"><line x1="6" y1="6" x2="421" y2="6" stroke="#b9b9b9" stroke-width="1.5"/><path d="M0 6l8-4v8zM427 6l-8-4v8z" fill="#b9b9b9"/><circle cx="213" cy="6" r="3" fill="#b9b9b9"/></svg></div>

  <div class="abs bridal" style="left:42px;top:429px">
    <div class="head">On-Site @ Brovique</div>
    <div class="list">
      <div class="row"><span>Bridal Make-up Trial</span><span>$95.00</span></div>
      <div class="row"><span>Bride Day-of Make-up</span><span>$125.00</span></div>
      <div class="row"><span>Bridesmaids/MOB/MOG</span><span>$75.00 each</span></div>
      <div class="row"><span>Flower Girl (Under 12 years old)</span><span>$50.00</span></div>
      <div class="row"><span>Add-ons - Strip or Cluster</span><span></span></div>
      <div class="row"><span>Lash Extentions</span><span>$20.00</span></div>
    </div>
  </div>
  <div class="photo" role="img" aria-label="Portrait photo of the studio's makeup artist" style="left:323px;top:452px;width:125px;height:148px"></div>

  <div class="abs bridal" style="left:42px;top:556px">
    <div class="head">Travel</div>
    <div class="list">
      <div class="row"><span>Bride Day-of makeup</span><span>$150.00</span></div>
      <div class="row"><span>Bridesmaids/MOB/MOG</span><span>$95.00 each</span></div>
      <div class="row"><span>Flower Girl (Under 12 years old)</span><span>$50.00</span></div>
    </div>
    <div class="list" style="margin-top:15.8px">There’s also a travel fee of $50.00<br>an hour per makeup artist.</div>
  </div>
  <div class="script" style="top:627px">Brovique Makeup Artists<br>Will Also Come To You!</div>

  <div class="divider" style="left:43px;width:427px;top:676px"><svg viewBox="0 0 427 12" preserveAspectRatio="none"><line x1="6" y1="6" x2="421" y2="6" stroke="#b9b9b9" stroke-width="1.5"/><path d="M0 6l8-4v8zM427 6l-8-4v8z" fill="#b9b9b9"/><circle cx="213" cy="6" r="3" fill="#b9b9b9"/></svg></div>

  <div class="eye" role="img" aria-label="Close-up photo of an eye before lash extensions" style="left:62px"></div>
  <svg class="abs" style="left:249px;top:774px" width="17" height="28" viewBox="0 0 17 28"><path d="M0 0L17 14L0 28Z" fill="#f4a88c"/></svg>
  <div class="eye" role="img" aria-label="Close-up photo of the same eye after lash extensions" style="left:277px"></div>

  <div class="divider" style="left:43px;width:427px;top:883px"><svg viewBox="0 0 427 12" preserveAspectRatio="none"><line x1="6" y1="6" x2="421" y2="6" stroke="#b9b9b9" stroke-width="1.5"/><path d="M0 6l8-4v8zM427 6l-8-4v8z" fill="#b9b9b9"/><circle cx="213" cy="6" r="3" fill="#b9b9b9"/></svg></div>

  <div class="abs contact" style="left:46px;top:908px">
    <div class="head" style="font-size:14px;margin-bottom:2px">Contact Us</div>
    <div class="row"><span>Text.</span><b>610 - 555 - 0143</b></div>
    <div class="row"><span>Call.</span><b>610-555-0178</b></div>
    <div class="row" style="line-height:18px;margin-top:4px"><span>Address.</span><b>1840 Harlow Lane,<br>Doylestown, PA 18901</b></div>
  </div>
  <div class="partner">SUMMIT LASHES</div>
  <div class="partner-box"></div>
</section>

</body>
</html>
```